BRAMBLE CABS

Taxi card design

Need changes very slow in replying to my messages.

Target Market(s)

Customers

Industry/Entity Type

Taxi

Contact Information for Business Card

See previous design

Font styles to use
Sans Serif

Colors
A7469A
B969AE
D3A5CF
EDDBEB
F8F0F9
6B429C
8869AF
B7A5CE
E3DAEB
F3F0F8

Requirements
Nice to have
• We are in the business of looking after people, not just driving vehicles front
Should not have
• Front number 01832 419 526 needs to big big

```html
<!DOCTYPE html>
<html lang="en">
<head>
<meta charset="utf-8">
<title>Bramble Cabs – Business Card</title>
<link rel="stylesheet" href="https://fonts.googleapis.com/css2?family=Roboto:wght@400;500;700&family=Orbitron:wght@800&display=swap">
<style>
  :root {
    --stage: #333333;
    --white: #ffffff;
    --ink: #111111;
    --black: #000000;
    --plum: #A7469A;
    --violet: #6B429C;
    --violet-mid: #8869AF;
    --band: linear-gradient(120deg, #6B429C 0%, #8A3A94 45%, #A7469A 100%);
  }
  * { box-sizing: border-box; margin: 0; padding: 0; }
  html, body {
    width: 1075px; height: 1200px; overflow: hidden;
    background: var(--stage);
    font-family: "Roboto", Arial, sans-serif;
  }
  .card {
    position: absolute; left: 206px; width: 663px;
    box-shadow: 3px 3px 3px rgba(0,0,0,.55);
    overflow: hidden;
  }
  /* back side */
  .card--back { top: 187px; height: 395px; background: var(--white); }
  .brand {
    position: absolute; display: flex; align-items: center; gap: 12px;
    font-weight: 700; letter-spacing: .5px; white-space: nowrap;
  }
  .brand__mark { display: block; border-radius: 6px; }
  .card--back .brand { right: 42px; top: 68px; font-size: 50px; color: var(--ink); }
  .card--back .brand__mark { width: 40px; height: 40px; background: var(--plum); }
  .phone-list { position: absolute; left: 35px; top: 178px; list-style: none; }
  .phone-list li {
    display: flex; align-items: center; gap: 10px;
    font-size: 19px; color: var(--ink); height: 23px; letter-spacing: .3px;
  }
  .icon {
    width: 26px; height: 20px; border-radius: 3px; flex: none;
    display: flex; align-items: center; justify-content: center;
  }
  .icon svg { width: 15px; height: 15px; }
  .icon--purple { background: var(--plum); color: var(--white); }
  .icon--white { background: var(--white); color: var(--violet); }
  .rule { position: absolute; left: 35px; top: 259px; width: 173px; height: 7px; background: var(--black); }
  .info-band {
    position: absolute; left: 0; bottom: 0; width: 100%; height: 131px;
    background: var(--band); color: var(--white);
  }
  .contact-list { position: absolute; left: 35px; top: 30px; list-style: none; }
  .contact-list li {
    display: flex; align-items: center; gap: 9px;
    font-size: 19px; height: 24px;
  }
  .address { position: absolute; left: 355px; top: 33px; display: flex; gap: 10px; }
  .address p { font-size: 19px; line-height: 23px; font-style: normal; }
  /* front side */
  .card--front { top: 637px; height: 396px; background: var(--band); }
  .card--front .brand { left: 50%; transform: translateX(-50%); top: 125px; font-size: 64px; color: var(--white); }
  .card--front .brand__mark { width: 50px; height: 50px; background: var(--white); border-radius: 8px; }
  .services {
    position: absolute; left: 0; width: 100%; top: 285px; text-align: center;
    color: var(--white); font-size: 19px; letter-spacing: .3px;
  }
  .services span::before { content: "●"; margin: 0 5px; font-size: 15px; }
  .services span:first-child::before { content: none; }
  .hotline {
    position: absolute; left: 0; bottom: 0; width: 100%; height: 69px;
    background: var(--black); display: flex; align-items: center; justify-content: center; gap: 16px;
  }
  .hotline .icon { width: 46px; height: 36px; border-radius: 3px; }
  .hotline .icon svg { width: 26px; height: 26px; }
  .hotline__number { font-family: "Orbitron", "Arial Black", sans-serif; font-weight: 800; font-size: 34px; color: var(--white); letter-spacing: 2px; }
</style>
</head>
<body>
<svg width="0" height="0" style="position:absolute">
  <symbol id="i-phone" viewBox="0 0 24 24"><path fill="currentColor" d="M6.6 10.8a15.1 15.1 0 0 0 6.6 6.6l2.2-2.2c.3-.3.7-.4 1-.2 1.1.4 2.3.6 3.6.6.6 0 1 .4 1 1V20c0 .6-.4 1-1 1A17 17 0 0 1 3 4c0-.6.4-1 1-1h3.5c.6 0 1 .4 1 1 0 1.3.2 2.5.6 3.6.1.3 0 .7-.2 1z"/><path fill="none" stroke="currentColor" stroke-width="1.6" stroke-linecap="round" d="M14 3.5a7 7 0 0 1 6.5 6.5M14 7a3.5 3.5 0 0 1 3 3"/></symbol>
  <symbol id="i-mail" viewBox="0 0 24 24"><rect x="3" y="5" width="18" height="14" rx="1" fill="none" stroke="currentColor" stroke-width="2"/><path d="M3 6l9 7 9-7" fill="none" stroke="currentColor" stroke-width="2"/></symbol>
  <symbol id="i-web" viewBox="0 0 24 24"><g fill="none" stroke="currentColor" stroke-width="1.8"><circle cx="12" cy="12" r="9"/><ellipse cx="12" cy="12" rx="4" ry="9"/><path d="M3 12h18M5 7h14M5 17h14"/></g></symbol>
  <symbol id="i-pin" viewBox="0 0 24 24"><path fill="currentColor" d="M12 2a7 7 0 0 0-7 7c0 5 7 13 7 13s7-8 7-13a7 7 0 0 0-7-7zm0 9.5A2.5 2.5 0 1 1 12 6.5a2.5 2.5 0 0 1 0 5z"/></symbol>
</svg>

<section class="card card--back">
  <div class="brand"><span class="brand__mark"></span>Bramble Cabs</div>
  <ul class="phone-list">
    <li><span class="icon icon--purple"><svg><use href="#i-phone"/></svg></span>01832 41 66 10</li>
    <li><span class="icon icon--purple"><svg><use href="#i-phone"/></svg></span>01832 30 30 30</li>
    <li><span class="icon icon--purple"><svg><use href="#i-phone"/></svg></span>01832 41 77 22</li>
  </ul>
  <div class="rule"></div>
  <div class="info-band">
    <ul class="contact-list">
      <li><span class="icon icon--white"><svg><use href="#i-phone"/></svg></span>Freephone: 0800 555 0 184</li>
      <li><span class="icon icon--white"><svg><use href="#i-mail"/></svg></span>ride@bramblecabs.example</li>
      <li><span class="icon icon--white"><svg><use href="#i-web"/></svg></span>www.bramblecabs.example</li>
    </ul>
    <address class="address">
      <span class="icon icon--white"><svg><use href="#i-pin"/></svg></span>
      <p>Elm Chapel Hall,<br>Market Row Thornby<br>TB4 7QX</p>
    </address>
  </div>
</section>

<section class="card card--front">
  <div class="brand"><span class="brand__mark"></span>Bramble Cabs</div>
  <p class="services"><span>AIRPORT TRANSFERS</span><span>MINIBUSES</span><span>SCHOOL TRANSPORT</span></p>
  <div class="hotline">
    <span class="icon icon--purple"><svg><use href="#i-phone"/></svg></span>
    <span class="hotline__number">01832 419 526</span>
  </div>
</section>
</body>
</html>
```